IT Company Business Card Rebranding

We want to modernize our business cards massively. We want to incorporate aspects of our old business card such as the white and geometric design with the blues of another icon. Existing Logo, old business card and icon are all attached.

We are a modern IT company that provides support for new and growing technologies and want our business cards to be modern yet professional.
Updates

Note: Do not use file ICON.png in design. This is just a design we like Added Wednesday, March 9, 2016

Industry/Entity Type

Information Technology

Contact Information for Business Card

Roughly 43 : 26 or 1075 x 650 px

Font styles to use
Serif

Colors
0492cd
3276b5
33a6d7
86cfc6
cfeae6
cee9f5
ffffff

Requirements
Must have
• Modern yet professional
Nice to have
• We would like to incorporate the blues of our existing logo and of the icon provided. Really like the design of the icon.
Should not have
• Too Decorative. Just simple and professional.
• Not have the circle icon, as it is a copyrighted icon, I just like the colors and the geometric design

```html
<!DOCTYPE html>
<html lang="en">
<head>
<meta charset="utf-8">
<title>Novaline Tech – Business Card</title>
<link href="https://fonts.googleapis.com/css2?family=Roboto:wght@300;400;500&display=swap" rel="stylesheet">
<style>
  :root {
    --page-bg: #e9ecef;
    --card-bg: #ffffff;
    --blue-dark: #2b55c9;
    --blue-mid: #3276b5;
    --blue-light: #33a6d7;
    --accent-gray: #a3a3a3;
    --text-name: #2f63d3;
    --text-title: #9a9a9a;
    --text-body: #5a5a5a;
    --logo-text: #8c8c8c;
    --divider: #d9d9d9;
  }
  * { margin: 0; padding: 0; box-sizing: border-box; }
  html, body {
    width: 1200px;
    height: 950px;
    overflow: hidden;
    background: var(--page-bg);
    font-family: "Roboto", Arial, sans-serif;
  }
  .stage {
    width: 1200px;
    height: 950px;
    display: flex;
    align-items: center;
    justify-content: center;
  }
  .business-card {
    position: relative;
    width: 1000px;
    height: 605px;
    background: var(--card-bg);
    box-shadow: 0 10px 30px rgba(0, 0, 0, 0.15);
    overflow: hidden;
  }
  .brand {
    position: absolute;
    left: 60px;
    top: 290px;
    width: 420px;
    display: flex;
    align-items: center;
    justify-content: center;
    gap: 18px;
  }
  .brand-dot {
    width: 22px;
    height: 22px;
    border-radius: 50%;
    background: var(--blue-mid);
  }
  .brand-name {
    font-size: 40px;
    font-weight: 300;
    letter-spacing: 8px;
    color: var(--logo-text);
    text-transform: uppercase;
  }
  .divider {
    position: absolute;
    left: 545px;
    top: 110px;
    width: 2px;
    height: 230px;
    background: linear-gradient(to bottom, rgba(217,217,217,0), var(--divider) 25%, var(--divider) 75%, rgba(217,217,217,0));
  }
  .contact {
    position: absolute;
    left: 590px;
    top: 120px;
  }
  .contact-name {
    font-size: 36px;
    font-weight: 500;
    color: var(--text-name);
    line-height: 1.1;
  }
  .contact-title {
    font-size: 24px;
    font-weight: 400;
    color: var(--text-title);
    margin-top: 4px;
  }
  .contact-list {
    list-style: none;
    margin-top: 30px;
  }
  .contact-item {
    display: flex;
    align-items: center;
    gap: 16px;
    font-size: 24px;
    color: var(--text-body);
    line-height: 1;
    margin-bottom: 14px;
  }
  .contact-icon {
    width: 22px;
    height: 22px;
    flex: none;
  }
  .band-blue {
    position: absolute;
    left: 0;
    bottom: 0;
    width: 715px;
    height: 36px;
    background: linear-gradient(to right, var(--blue-dark), var(--blue-light) 70%, var(--blue-dark));
  }
  .band-gray {
    position: absolute;
    left: 723px;
    bottom: 0;
    right: 0;
    height: 36px;
    background: var(--accent-gray);
  }
</style>
</head>
<body>
<main class="stage">
  <section class="business-card">
    <div class="brand">
      <span class="brand-dot"></span>
      <span class="brand-name">Novaline Tech</span>
    </div>

    <div class="divider"></div>

    <div class="contact">
      <h1 class="contact-name">Mara Quill</h1>
      <p class="contact-title">President</p>
      <ul class="contact-list">
        <li class="contact-item">
          <svg class="contact-icon" viewBox="0 0 24 24" aria-hidden="true">
            <path fill="#2f63d3" d="M6.6 10.8a15.1 15.1 0 0 0 6.6 6.6l2.2-2.2a1 1 0 0 1 1-.25 11.4 11.4 0 0 0 3.6.57 1 1 0 0 1 1 1V20a1 1 0 0 1-1 1A17 17 0 0 1 3 4a1 1 0 0 1 1-1h3.5a1 1 0 0 1 1 1c0 1.25.2 2.45.57 3.6a1 1 0 0 1-.25 1z"/>
          </svg>
          <span>555 0142 7781</span>
        </li>
        <li class="contact-item">
          <svg class="contact-icon" viewBox="0 0 24 24" aria-hidden="true">
            <rect x="2" y="5" width="20" height="14" rx="2" fill="#2f63d3"/>
            <path d="M3 6.5l9 6.5 9-6.5" fill="none" stroke="#ffffff" stroke-width="1.6"/>
          </svg>
          <span>mara@novaline.net</span>
        </li>
        <li class="contact-item">
          <svg class="contact-icon" viewBox="0 0 24 24" aria-hidden="true">
            <circle cx="12" cy="12" r="10" fill="#2f63d3"/>
            <path d="M2 12h20M12 2c3 3 3 17 0 20M12 2c-3 3-3 17 0 20" fill="none" stroke="#ffffff" stroke-width="1.3"/>
          </svg>
          <span>www.novaline.net</span>
        </li>
      </ul>
    </div>

    <div class="band-blue"></div>
    <div class="band-gray"></div>
  </section>
</main>
</body>
</html>
```